BrackettPainting Business Cards

Create high resolution (300dpi+) Business card. Attached is an old business card that is simple, but doesn't need to the same design. No pastel colors, no generic clip art. The text to include:
Brackett Painting
Dave Brackett
Residential & Commercial
Interior & Exterior
502-555-0178
davebrack@quorvex.com

```html
<!DOCTYPE html>
<html lang="en">
<head>
<meta charset="utf-8">
<title>Brackett Painting – Business Card</title>
<link rel="stylesheet" href="https://fonts.googleapis.com/css2?family=IM+Fell+English+SC&family=Pinyon+Script&family=Alfa+Slab+One&display=swap">
<style>
  :root {
    --page-bg: #e6e9ed;
    --card-top: #f4f6f8;
    --card-bottom: #e3e8ee;
    --brand-red: #9a2f1f;
    --script-red: #8a2a1c;
    --band-red: rgba(126, 38, 22, 0.88);
    --name-light: #e2d6d0;
    --phone-light: #c3c6d0;
  }
  * { margin: 0; padding: 0; box-sizing: border-box; }
  html, body {
    width: 1200px;
    height: 900px;
    overflow: hidden;
    background: var(--page-bg);
  }
  .card {
    position: absolute;
    left: 75px;
    top: 150px;
    width: 1050px;
    height: 600px;
    background: linear-gradient(180deg, var(--card-top), var(--card-bottom));
    border-radius: 6px;
    box-shadow: 0 10px 30px rgba(0, 0, 0, 0.12);
    overflow: hidden;
  }
  .brand-line {
    position: absolute;
    font-family: "IM Fell English SC", serif;
    text-transform: uppercase;
    color: var(--brand-red);
    font-size: 88px;
    line-height: 1;
    letter-spacing: 2px;
    white-space: nowrap;
    text-shadow: 0 0 2px rgba(255, 255, 255, 0.9);
  }
  .brand-first { left: 34px; top: 66px; }
  .brand-second { left: 472px; top: 146px; }
  .services {
    position: absolute;
    left: 0;
    width: 100%;
    text-align: center;
    font-family: "Pinyon Script", cursive;
    color: var(--script-red);
    font-size: 42px;
    line-height: 1;
    white-space: nowrap;
    padding-left: 70px;
  }
  .services-type { top: 280px; }
  .services-scope { top: 336px; }
  .contact-band {
    position: absolute;
    left: 0;
    top: 459px;
    width: 100%;
    height: 90px;
    background: var(--band-red);
    display: flex;
    align-items: center;
    justify-content: space-between;
    padding: 0 41px 0 52px;
    font-family: "Alfa Slab One", serif;
    font-size: 40px;
    white-space: nowrap;
  }
  .contact-name { color: var(--name-light); }
  .contact-phone { color: var(--phone-light); }
  .contact-email {
    position: absolute;
    left: 0;
    top: 560px;
    width: 100%;
    text-align: center;
    font-family: "Alfa Slab One", serif;
    font-size: 24px;
    line-height: 1;
    color: var(--brand-red);
    white-space: nowrap;
  }
</style>
</head>
<body>
  <div class="card">
    <div class="brand-line brand-first">Brackett</div>
    <div class="brand-line brand-second">Painting</div>
    <div class="services services-type">Residential &amp; Commercial</div>
    <div class="services services-scope">Interior &amp; Exterior</div>
    <div class="contact-band">
      <span class="contact-name">Dave Brackett</span>
      <span class="contact-phone">502-555-0178</span>
    </div>
    <div class="contact-email">davebrack@quorvex.com</div>
  </div>
</body>
</html>
```